Business Cards - Brightway Harbor

need to design unique business card for my mortgage business. I need to design credit card style business card for my business or any unique idea that you might have

Target Market(s)

Home Loan customers

Industry/Entity Type

Mortgage Brokerage

Contact Information for Business Card

please design credit card style or very unique style business card

Colors

Designer to choose colors to be used in the design.

Requirements
Must have
• Name
• position
• Phone number
• fax number
• email address
• website address
• social media address
• All above fields will be provided once design in finalised

```html
<!DOCTYPE html>
<html lang="en">
<head>
<meta charset="utf-8">
<title>Brightway Harbor – Business Cards</title>
<link rel="stylesheet" href="https://fonts.googleapis.com/css2?family=Libre+Baskerville:wght@400&family=Roboto+Condensed:wght@400&display=swap">
<style>
  :root {
    --page-bg: #e6e8ec;
    --royal-blue: #1033c8;
    --sky-blue: #1f9fd6;
    --card-white: #ffffff;
    --photo-dark: #3c3f44;
    --photo-mid: #6d6a68;
    --photo-warm: #9a8577;
    --text-white: #ffffff;
  }
  * { margin: 0; padding: 0; box-sizing: border-box; }
  html, body { width: 1200px; height: 900px; overflow: hidden; }
  body {
    background: var(--page-bg);
    position: relative;
    font-family: "Roboto Condensed", sans-serif;
  }
  .card {
    position: absolute;
    width: 600px;
    height: 343px;
    border-radius: 6px;
    overflow: hidden;
    box-shadow: 0 10px 28px rgba(0,0,0,.22);
  }
  /* front */
  .card-front { left: 60px; top: 70px; }
  .front-photo {
    position: absolute; inset: 0;
    background:
      linear-gradient(160deg, rgba(40,42,46,.75) 0%, rgba(40,42,46,.35) 55%, rgba(40,42,46,.7) 100%),
      linear-gradient(120deg, var(--photo-dark) 0%, var(--photo-mid) 45%, var(--photo-warm) 75%, var(--photo-mid) 100%);
  }
  .front-brand {
    position: absolute; right: 34px; top: 40px;
    color: var(--text-white);
  }
  .brand-mark {
    display: inline-flex; align-items: center; gap: 12px;
    font-family: "Libre Baskerville", serif;
    font-size: 34px; line-height: 1;
  }
  .brand-dot { width: 22px; height: 22px; border-radius: 50%; background: currentColor; }
  /* back */
  .card-back { left: 540px; top: 480px; background: var(--card-white); }
  .back-band { position: absolute; inset: 0; width: 100%; height: 100%; }
  .back-brand {
    position: absolute; left: 0; right: 0; top: 60px;
    text-align: center;
  }
  .back-brand .brand-mark { color: var(--royal-blue); font-size: 36px; }
  .back-brand .brand-dot { background: var(--sky-blue); }
  .contact {
    position: absolute; color: var(--text-white);
    font-size: 19px; line-height: 1.35;
  }
  .contact-person { left: 30px; bottom: 26px; }
  .contact-office { right: 30px; top: 190px; text-align: right; }
  .social-row {
    position: absolute; right: 30px; bottom: 28px;
    display: flex; gap: 10px; list-style: none;
  }
  .social-row li {
    width: 24px; height: 24px; border-radius: 50%;
    border: 2px solid var(--text-white);
  }
</style>
</head>
<body>
  <section class="card card-front">
    <div class="front-photo" role="img" aria-label="Photo of a model house beside hands signing a home loan contract with house keys"></div>
    <div class="front-brand">
      <div class="brand-mark"><span class="brand-dot"></span>Brightway Harbor</div>
    </div>
  </section>

  <section class="card card-back">
    <svg class="back-band" viewBox="0 0 600 343" preserveAspectRatio="none" aria-hidden="true">
      <polygon points="0,215 600,118 600,343 0,343" fill="var(--royal-blue)"/>
    </svg>
    <div class="back-brand">
      <div class="brand-mark"><span class="brand-dot"></span>Brightway Harbor</div>
    </div>
    <div class="contact contact-person">
      <p>Name</p>
      <p>Position</p>
      <p>Phone number</p>
    </div>
    <div class="contact contact-office">
      <p>Fax number</p>
      <p>E-mail address</p>
      <p>www.websiteaddress.com</p>
    </div>
    <ul class="social-row" aria-label="Social media links">
      <li></li><li></li><li></li><li></li><li></li><li></li>
    </ul>
  </section>
</body>
</html>
```